Accounting firm needing business card / letterhead designed
Marcus T. Elbering, CPA
marcus@fernquill.com
www.fernquill.com
482 N Harlow Ave Halverton, NV 43719
775-555-0172

```html
<!DOCTYPE html>
<html lang="en">
<head>
<meta charset="utf-8">
<title>Fernquill Advisory – Business Card</title>
<link href="https://fonts.googleapis.com/css2?family=Oxygen:wght@400;700&display=swap" rel="stylesheet">
<style>
  :root {
    --backdrop: #2b2b2d;
    --card-white: #ffffff;
    --card-black: #1c1c1d;
    --navy: #2b2a72;
    --green: #8cc63f;
    --grey: #6b6b70;
  }
  * { box-sizing: border-box; margin: 0; padding: 0; }
  html, body {
    width: 1200px; height: 900px; overflow: hidden;
    background: var(--backdrop);
    font-family: "Oxygen", Arial, sans-serif;
  }
  .stage {
    width: 1200px; height: 900px;
    display: flex; flex-direction: column;
    align-items: center; justify-content: center; gap: 56px;
  }
  .card {
    width: 580px; height: 331px;
    position: relative;
    box-shadow: 0 14px 30px rgba(0,0,0,.45);
  }
  .card--back {
    background: var(--card-black);
    display: flex; align-items: center; justify-content: center;
  }
  .card--front { background: var(--card-white); }

  .wordmark {
    font-weight: 700; color: var(--navy);
    text-transform: uppercase; line-height: 1;
    display: flex; flex-direction: column; align-items: flex-start;
  }
  .wordmark__main { font-size: 44px; letter-spacing: 1px; }
  .wordmark__sub { font-size: 13.5px; letter-spacing: 5.6px; margin-top: 6px; }
  .card--back .wordmark__main { font-size: 38px; }
  .card--back .wordmark__sub { font-size: 11.5px; letter-spacing: 4.8px; }

  .card--front .wordmark {
    position: absolute; left: 34px; top: 128px;
  }
  .divider {
    position: absolute; left: 318px; top: 88px;
    width: 2px; height: 158px; background: var(--green);
  }
  .contact {
    position: absolute; left: 342px; top: 92px;
    color: var(--grey);
  }
  .contact__name { font-size: 19px; font-weight: 700; color: var(--navy); }
  .contact__title { font-size: 13px; color: var(--navy); margin-top: 1px; }
  .contact__address { font-size: 13px; line-height: 17px; margin-top: 14px; }
  .contact__list { list-style: none; margin-top: 8px; font-size: 13px; }
  .contact__list li { display: flex; align-items: center; gap: 12px; height: 20px; }
  .contact__list svg { width: 14px; height: 14px; flex: none; }
</style>
</head>
<body>
<main class="stage">
  <section class="card card--back" aria-label="Card back">
    <div class="wordmark">
      <span class="wordmark__main">Fernquill</span>
      <span class="wordmark__sub">Advisory</span>
    </div>
  </section>

  <section class="card card--front" aria-label="Card front">
    <div class="wordmark">
      <span class="wordmark__main">Fernquill</span>
      <span class="wordmark__sub">Advisory</span>
    </div>
    <div class="divider"></div>
    <div class="contact">
      <p class="contact__name">Marcus T. Elbering</p>
      <p class="contact__title">CPA</p>
      <p class="contact__address">482 N Harlow Ave<br>Halverton, NV 43719</p>
      <ul class="contact__list">
        <li>
          <svg viewBox="0 0 14 14" aria-hidden="true"><rect x="3.5" y="0.8" width="7" height="12.4" rx="1.2" fill="none" stroke="#2b2a72" stroke-width="1.4"/><line x1="6" y1="11" x2="8" y2="11" stroke="#2b2a72" stroke-width="1.2"/></svg>
          <span>775-555-0172</span>
        </li>
        <li>
          <svg viewBox="0 0 14 14" aria-hidden="true"><rect x="0.8" y="3" width="12.4" height="8.5" fill="#2b2a72"/><polyline points="1,3.4 7,8 13,3.4" fill="none" stroke="#fff" stroke-width="1.1"/></svg>
          <span>marcus@fernquill.com</span>
        </li>
        <li>
          <svg viewBox="0 0 14 14" aria-hidden="true"><g fill="none" stroke="#2b2a72" stroke-width="1.2"><circle cx="7" cy="7" r="6"/><ellipse cx="7" cy="7" rx="2.6" ry="6"/><line x1="1" y1="7" x2="13" y2="7"/><line x1="2" y1="4" x2="12" y2="4"/><line x1="2" y1="10" x2="12" y2="10"/></g></svg>
          <span>www.fernquill.com</span>
        </li>
      </ul>
    </div>
  </section>
</main>
</body>
</html>
```